Web Design Project

We need a web design for a new company that we started called ZARN CNG. ZARN CNG is a company that will build, own and operate compressed natural gas fueling stations throughout the United States. Our primary customers are Trucking companies and the stations will be built for semi trucks. CNG is better for the environment than diesel fuel, and will save trucking companies loads of money. It is also a domestic product which means that it will create American jobs and help America become energy independent. I have attached a logo that we are using. We dont need to stay with this logo persay, but it is what we have for now. We have a video on Vidlo that shows a bit of what we are doing. just search for ZARN CNG. ZARN CNG is a sister company of Holtmark of Arizona,www.hkqvz.example and a nationwide distributor of TRIVEX FUEL, www.trivexfuel.example. We will need links to these sites. Please make any pictures of trucks Holtmark trucks, and please do not use pictures of cabover trucks.

Target Market(s)

The target market are truck drivers and truckers.

Industry/Entity Type

Environment

Requirements
Must have
• Map showing station locations, a page with industry news, a page with a savings calculator (we can code the calculator) Site should have links to

```html
<!DOCTYPE html>
<html lang="en">
<head>
<meta charset="utf-8">
<title>ZARN CNG</title>
<link rel="stylesheet" href="https://fonts.googleapis.com/css2?family=Gelasio:wght@400;700&family=Noto+Serif:wght@400&family=Roboto:wght@400;700&display=swap">
<style>
  :root {
    --green: #5aa02c;
    --green-bright: #26d04a;
    --ink: #1f1f1f;
    --text: #333;
    --bar: #141414;
    --nav: #1c1c1c;
    --panel: #f4f4f4;
    --panel-line: #dadada;
    --orange: #f2b23a;
    --footer-link: #b9b9b9;
  }
  * { box-sizing: border-box; margin: 0; padding: 0; }
  html, body { width: 960px; height: 1200px; overflow: hidden; background: #fff; }
  body { position: relative; font-family: "Gelasio", Georgia, serif; color: var(--text); }
  .abs { position: absolute; }

  .follow { left: 692px; top: 12px; font-size: 12px; font-weight: 700; color: var(--green); display: flex; align-items: center; gap: 6px; }
  .follow .social { width: 19px; height: 19px; border-radius: 4px; display: inline-block; }
  .follow span.label { margin-right: 2px; }
  .s1 { background: #3b5a9a; } .s2 { background: #4fb5e6; } .s3 { background: #444; } .s4 { background: #f08a24; }

  .brand { left: 88px; top: 38px; font-size: 44px; font-weight: 700; color: var(--green-bright); letter-spacing: 0.5px; line-height: 1; }
  .tagline { right: 82px; top: 58px; font-size: 22px; color: var(--ink); }

  .nav { left: 80px; top: 114px; width: 800px; height: 45px; background: var(--nav); border-radius: 4px 4px 0 0;
         display: flex; align-items: center; padding-left: 23px; font-size: 11.5px; color: #fff; }
  .nav a { color: #fff; text-decoration: none; }
  .nav .sep { margin: 0 23px; color: #ccc; }

  .hero { left: 80px; top: 159px; width: 800px; height: 342px;
          background: linear-gradient(160deg, #cfd5d6 0%, #a6aaad 35%, #8d3a3a 55%, #6a6c70 75%, #b4b8bb 100%); }
  .slide-box { left: 622px; top: 278px; width: 220px; height: 179px; background: rgba(20,20,20,0.85); border-radius: 3px; }
  .slide-title { left: 636px; top: 296px; font-size: 27px; line-height: 32px; color: #fff; }
  .slide-more { left: 773px; top: 377px; font-family: "Roboto", Arial, sans-serif; font-size: 10px; color: var(--green); letter-spacing: 0.5px; }
  .thumbs { left: 632px; top: 406px; display: flex; gap: 10px; }
  .thumbs i { width: 26px; height: 26px; display: block; }

  .searchbar { left: 80px; top: 501px; width: 800px; height: 35px; background: var(--bar); border-radius: 0 0 4px 4px; }
  .search-input { left: 90px; top: 510px; width: 272px; height: 18px; background: #f4f4f4; }
  .search-btn { left: 370px; top: 511px; font-size: 12px; color: #fff; }
  .callus { left: 645px; top: 506px; font-family: "Roboto", Arial, sans-serif; font-size: 19px; color: var(--orange); }

  .panel { background: var(--panel); border: 1px solid var(--panel-line); border-radius: 3px; }
  .panel-news { left: 80px; top: 546px; width: 495px; height: 216px; }
  .panel-video { left: 585px; top: 546px; width: 295px; height: 216px; }
  .heading { font-size: 21px; color: var(--green); }
  .news-item { left: 95px; width: 460px; }
  .news-img { position: absolute; left: 0; top: 0; width: 71px; height: 64px; border: 2px solid #d0d0d0; border-radius: 3px; }
  .news-text { position: absolute; left: 85px; top: 0; width: 375px; font-family: "Noto Serif", Georgia, serif; font-size: 10px; line-height: 16px; color: #333; }
  .news-date { position: absolute; left: 85px; top: 50px; font-family: "Roboto", Arial, sans-serif; font-size: 9.5px; color: var(--green); letter-spacing: 1px; }
  .news-more { position: absolute; left: 382px; top: 50px; font-family: "Roboto", Arial, sans-serif; font-size: 10px; color: var(--green); letter-spacing: 0.5px; }
  .divider { left: 100px; top: 667px; width: 454px; height: 1px; background: #d4d4d4; }

  .video { left: 595px; top: 582px; width: 274px; height: 164px; background: linear-gradient(120deg, #4fe082 0%, #55d9a8 50%, #6fd0e0 100%); }
  .video-controls { left: 595px; top: 733px; width: 274px; height: 13px; background: #1b1b1b; }
  .video-progress { left: 595px; top: 733px; width: 274px; height: 2px; background: #555; }
  .video-played { left: 595px; top: 733px; width: 18px; height: 2px; background: #e02020; }

  .about-img { left: 94px; top: 826px; width: 240px; height: 160px; background: linear-gradient(170deg, #3b3f42 0%, #7a8a74 40%, #2f7a3a 70%, #8e9295 100%); }
  .about-text { left: 352px; top: 823px; width: 514px; font-size: 10.5px; line-height: 16px; text-align: justify; color: #222; }

  .footer { left: 0; top: 1023px; width: 960px; height: 177px; background: linear-gradient(#2b2b2b, #050505); }
  .footer-links { left: 81px; top: 1039px; font-size: 11px; color: var(--footer-link); display: flex; }
  .footer-links .sep { margin: 0 15px; }
  .copyright { right: 82px; top: 1040px; font-size: 10.5px; color: var(--footer-link); }
</style>
</head>
<body>
  <header>
    <div class="abs follow"><span class="label">Follow us on :</span>
      <i class="social s1" role="img" aria-label="Social network link"></i>
      <i class="social s2" role="img" aria-label="Social network link"></i>
      <i class="social s3" role="img" aria-label="Social network link"></i>
      <i class="social s4" role="img" aria-label="Feed link"></i>
    </div>
    <div class="abs brand">ZARN CNG</div>
    <div class="abs tagline">Will Save Trucking Companies Loads of Money</div>
    <nav class="abs nav">
      <a>HOME</a><span class="sep">|</span><a>ABOUT US</a><span class="sep">|</span><a>WHATS NEW</a><span class="sep">|</span><a>TEAM</a><span class="sep">|</span><a>FOCUS</a><span class="sep">|</span><a>INDUSTRIES</a><span class="sep">|</span><a>SAVINGS</a><span class="sep">|</span><a>CONTACT US</a>
    </nav>
  </header>

  <section>
    <div class="abs hero" role="img" aria-label="Photo of red semi truck refueling at a natural gas station"></div>
    <div class="abs slide-box"></div>
    <div class="abs slide-title">Award-Winning<br>Reliability</div>
    <div class="abs slide-more">Readmore...</div>
    <div class="abs thumbs">
      <i role="img" aria-label="Slide thumbnail" style="background:#3d5fb0"></i>
      <i role="img" aria-label="Slide thumbnail" style="background:#3a8fd8"></i>
      <i role="img" aria-label="Slide thumbnail" style="background:#dcdcd4"></i>
      <i role="img" aria-label="Slide thumbnail" style="background:#b88a6a"></i>
      <i role="img" aria-label="Slide thumbnail" style="background:#c8b22a"></i>
      <i role="img" aria-label="Slide thumbnail" style="background:#3a8fd8"></i>
    </div>
    <div class="abs searchbar"></div>
    <div class="abs search-input"></div>
    <div class="abs search-btn">Search</div>
    <div class="abs callus">Call us now: 1800-55-0123</div>
  </section>

  <section>
    <div class="abs panel panel-news"></div>
    <div class="abs heading" style="left:93px;top:553px">Industry News</div>
    <article class="abs news-item" style="top:594px">
      <div class="news-img" role="img" aria-label="Photo of a CNG fuel nozzle" style="background:linear-gradient(135deg,#c8ccd0,#707880)"></div>
      <p class="news-text">Lorem ipsum dolor sit amet, consectetur adipisicing elit, sedeiu smod tempor incididunt. Lorem ipsum dolor sit amet, consectetur adipisicing smod tempor incididunt</p>
      <div class="news-date">02 - 01 - 2013</div>
      <div class="news-more">Readmore...</div>
    </article>
    <div class="abs divider"></div>
    <article class="abs news-item" style="top:684px">
      <div class="news-img" role="img" aria-label="Photo of a natural gas sign" style="background:linear-gradient(135deg,#b8d030,#2a2a2a)"></div>
      <p class="news-text">Lorem ipsum dolor sit amet, consectetur adipisicing elit, sedeiu smod tempor incididunt. Lorem ipsum dolor sit amet, consectetur adipisicing smod tempor incididunt</p>
      <div class="news-date">02 - 01 - 2013</div>
      <div class="news-more">Readmore...</div>
    </article>

    <div class="abs panel panel-video"></div>
    <div class="abs heading" style="left:594px;top:553px">Video</div>
    <div class="abs video" role="img" aria-label="Company video still in green and blue tones"></div>
    <div class="abs video-controls"></div>
    <div class="abs video-progress"></div>
    <div class="abs video-played"></div>
  </section>

  <section>
    <div class="abs heading" style="left:94px;top:775px">About Us</div>
    <div class="abs about-img" role="img" aria-label="Photo of green trucks at a covered CNG fueling station"></div>
    <p class="abs about-text">Lorem ipsum dolor sit amet, consectetur adipisicing elit, sed do eiusmod tempor incididunt ut labore et dolore magna aliqua. Ut enim ad minim veniam, quis nostrud exercitation ullamco laboris nisi ut aliquip ex ea commodo consequat. Lorem ipsum dolor sit amet, consectetur adipisicing elit, sed do eiusmod tempor incididunt ut labore et dolore magna aliqua. Ut enim ad minim veniam, quis nostrud exercitation ullamco laboris nisi ut aliquip ex ea commodo consequat.Lorem ipsum dolor sit amet, consectetur. Lorem ipsum dolor sit amet, consectetur adipisicing elit, sed do eiusmod tempor incididunt ut labore et dolore magna aliqua. Ut enim ad minim veniam, quis nostrud exercitation ullamco laboris nisi ut aliquip ex ea commodo consequat. Lorem ipsum dolor sit amet, consectetur adipisicing elit, sed do eiusmod tempor incididunt ut labore et dolore magna aliqua. Ut enim ad minim veniam, quis nostrud exercitation ullamco laboris nisi ut aliquip ex ea commodo consequat.Lorem ipsum dolor sit amet, consectetur</p>
  </section>

  <footer>
    <div class="abs footer"></div>
    <div class="abs footer-links">
      <span>Home</span><span class="sep">|</span><span>About Us</span><span class="sep">|</span><span>Whats New</span><span class="sep">|</span><span>Team</span><span class="sep">|</span><span>Focus</span><span class="sep">|</span><span>Industries</span><span class="sep">|</span><span>Savings</span><span class="sep">|</span><span>Contact Us</span>
    </div>
    <div class="abs copyright">Copyright © 2013 Zarn-CNG</div>
  </footer>
</body>
</html>
```